Brimovex business card

Based on company logo and website given , to design a business card temple. Slogan "Caring for every paw, every single day"
Color style please refer to our website

```html
<!DOCTYPE html>
<html lang="en">
<head>
<meta charset="utf-8">
<title>Brimovex business card</title>
<link rel="stylesheet" href="https://fonts.googleapis.com/css2?family=Poppins:wght@400;600&display=swap">
<style>
  :root {
    --backdrop: #e3dfd7;
    --forest: #0f4c4b;
    --forest-deep: #0a3433;
    --paper: #fbfbf9;
    --gold: #a3961c;
    --slate: #4a4a4a;
  }
  * { margin: 0; padding: 0; box-sizing: border-box; }
  html, body { width: 1200px; height: 800px; overflow: hidden; }
  body {
    background: var(--backdrop);
    font-family: "Poppins", sans-serif;
    display: flex;
    align-items: center;
    justify-content: center;
    gap: 60px;
  }
  .card {
    width: 490px;
    height: 280px;
    position: relative;
    box-shadow: 0 10px 30px rgba(0,0,0,0.12);
  }
  .card--front {
    background: linear-gradient(160deg, var(--forest) 0%, var(--forest-deep) 100%);
    display: flex;
    flex-direction: column;
    align-items: center;
    justify-content: center;
    gap: 14px;
  }
  .wordmark {
    color: var(--gold);
    font-weight: 600;
    letter-spacing: -0.5px;
    line-height: 1;
  }
  .card--front .wordmark { font-size: 40px; }
  .slogan {
    color: var(--gold);
    font-size: 14px;
    font-weight: 400;
    letter-spacing: 0.2px;
  }
  .card--back {
    background: var(--paper);
    display: flex;
    align-items: center;
    padding: 0 34px 0 40px;
  }
  .card--back .wordmark { font-size: 34px; width: 215px; }
  .details { flex: 1; }
  .person-name {
    color: var(--gold);
    font-weight: 600;
    font-size: 24px;
    line-height: 1.1;
  }
  .person-role {
    color: var(--slate);
    font-size: 13px;
    margin-top: 2px;
  }
  .divider {
    width: 22px;
    height: 2px;
    background: var(--gold);
    margin: 8px 0 16px;
  }
  .contact-row {
    display: flex;
    align-items: flex-start;
    gap: 12px;
    margin-bottom: 10px;
    color: var(--gold);
    font-size: 11.5px;
    line-height: 1.35;
  }
  .contact-row svg { width: 15px; height: 15px; flex: none; margin-top: 2px; fill: var(--gold); }
</style>
</head>
<body>
  <section class="card card--front">
    <div class="wordmark">Brimovex</div>
    <p class="slogan">Caring for every paw, every single day</p>
  </section>

  <section class="card card--back">
    <div class="wordmark">Brimovex</div>
    <div class="details">
      <h1 class="person-name">Marcus Hale</h1>
      <p class="person-role">Manager</p>
      <div class="divider"></div>

      <div class="contact-row">
        <svg viewBox="0 0 24 24" aria-hidden="true"><path d="M6.6 10.8a15.1 15.1 0 0 0 6.6 6.6l2.2-2.2a1 1 0 0 1 1-.25 11.4 11.4 0 0 0 3.6.57 1 1 0 0 1 1 1V20a1 1 0 0 1-1 1A17 17 0 0 1 3 4a1 1 0 0 1 1-1h3.5a1 1 0 0 1 1 1c0 1.25.2 2.45.57 3.570a1 1 0 0 1-.25 1z"/></svg>
        <div>1800 403 719<br>1800 403 719</div>
      </div>

      <div class="contact-row">
        <svg viewBox="0 0 24 24" aria-hidden="true"><path d="M12 2a10 10 0 1 0 0 20 10 10 0 0 0 0-20zm6.9 6h-3a15.6 15.6 0 0 0-1.4-3.6A8 8 0 0 1 18.9 8zM12 4a14 14 0 0 1 1.9 4h-3.8A14 14 0 0 1 12 4zM4.3 14a8 8 0 0 1 0-4h3.4a16.5 16.5 0 0 0 0 4zm.8 2h3a15.6 15.6 0 0 0 1.4 3.6A8 8 0 0 1 5.1 16zm3-8h-3a8 8 0 0 1 4.4-3.6A15.6 15.6 0 0 0 8.1 8zM12 20a14 14 0 0 1-1.9-4h3.8A14 14 0 0 1 12 20zm2.3-6H9.7a14.7 14.7 0 0 1 0-4h4.6a14.7 14.7 0 0 1 0 4zm.2 5.6a15.6 15.6 0 0 0 1.4-3.6h3a8 8 0 0 1-4.4 3.6zm1.8-5.6a16.5 16.5 0 0 0 0-4h3.4a8 8 0 0 1 0 4z"/></svg>
        <div>www.brimovex.com.au<br>sales@brimovex.com.au</div>
      </div>

      <div class="contact-row">
        <svg viewBox="0 0 24 24" aria-hidden="true"><path d="M12 2a7 7 0 0 0-7 7c0 5.2 7 13 7 13s7-7.8 7-13a7 7 0 0 0-7-7zm0 9.5A2.5 2.5 0 1 1 12 6.5a2.5 2.5 0 0 1 0 5z"/></svg>
        <div>4/22 Harlow Street<br>Ashgrove Vic 3152</div>
      </div>
    </div>
  </section>
</body>
</html>
```